Infographic for open source project (over-the-air updates for connected devices)

We would like an infographic created. It can be 1-2 pages. Our project is targeted toward the Internet of Things (connected devices), as it provides a secure and robust way to deploy over-the-air (OTA) software updates for connected Linux devices. This has been broken into 4 broad categories with specific requirements within each.

Please see some content on our website to better understand our design preference:

https://voltrix.example/resources/customer-case-studies
Updates

Target Market(s)

Embedded system developers, owners of connected device projects (e.g. developers of home automation, industrial automation, smart energy, smart appliances,

Industry/Entity Type

Internet

Requirements
Must have
• Must include all the content included in the xls file attached. Design should follow our StyleGuide (also attached) and the general design aesthetic (e.g. our customer case studies), but creativity is encouraged for the infographic to best present the information in the xls file.

```html
<!DOCTYPE html>
<html lang="en">
<head>
<meta charset="utf-8">
<title>Voltrix – Requirements for robust OTA software updates</title>
<link rel="stylesheet" href="https://fonts.googleapis.com/css2?family=Montserrat:wght@600;700;800&family=Open+Sans:wght@400;600;700&display=swap">
<style>
  :root{
    --plum-900:#5c1a47;
    --plum-800:#6a2555;
    --plum-700:#7b3665;
    --plum-600:#8c4b77;
    --plum-500:#9e6790;
    --plum-300:#b08aa6;
    --teal-900:#1d5a6d;
    --teal-800:#2e6d80;
    --teal-600:#5c8e9d;
    --slate-800:#59585d;
    --slate-600:#78777c;
    --slate-700:#6d6c70;
    --orange:#f6a01e;
    --orange-red:#e84c2a;
    --panel:#e3e3e5;
    --panel-light:#efeff0;
    --ink:#2a2a2c;
    --head-teal:#1f4450;
    --mark:#a2a2a5;
    --white:#ffffff;
  }
  *{box-sizing:border-box;margin:0;padding:0}
  html,body{width:1200px;height:930px;overflow:hidden;background:var(--white)}
  body{position:relative;font-family:"Open Sans",Arial,sans-serif;color:var(--ink)}

  .folder{position:absolute;left:0;top:0}

  .brand{position:absolute;left:128px;top:118px;display:flex;align-items:center;gap:14px}
  .brand-dot{width:38px;height:38px;border-radius:50%;background:var(--teal-900)}
  .brand-name{font-family:"Montserrat",Arial,sans-serif;font-weight:800;font-size:46px;color:var(--plum-900);letter-spacing:.5px}

  .category{position:absolute;top:206px;width:168px;height:68px;border:2px solid var(--white);
    display:flex;align-items:center;justify-content:center;text-align:center;
    font-family:"Montserrat",Arial,sans-serif;font-weight:700;font-size:15.5px;line-height:1.2;color:var(--white)}
  .category--robust{left:384px;background:var(--plum-900)}
  .category--integration{left:566px;background:var(--teal-900)}
  .category--security{left:763px;background:var(--slate-700)}
  .category--fleet{left:955px;background:var(--plum-900)}

  .connectors{position:absolute;left:0;top:0;pointer-events:none}

  .req-table{position:absolute}
  .req-table--robust{left:76px;top:318px;width:338px}
  .req-table--integration{left:434px;top:318px;width:334px}
  .req-table--security{left:434px;top:588px;width:334px}
  .req-table--fleet{left:790px;top:318px;width:340px}

  .req-table--robust .table-head,.req-table--robust .req-row{grid-template-columns:90px 134px 114px}
  .req-table--integration .table-head,.req-table--integration .req-row,
  .req-table--security .table-head,.req-table--security .req-row{grid-template-columns:95px 108px 131px}
  .req-table--fleet .table-head,.req-table--fleet .req-row{grid-template-columns:96px 120px 124px}

  .table-head{display:grid;align-items:center;height:28px;margin-bottom:2px;
    font-family:"Montserrat",Arial,sans-serif;font-weight:700;font-size:12px;line-height:1.1;text-align:center;color:var(--plum-900)}
  .req-table--integration .table-head{color:var(--head-teal)}
  .req-table--security .table-head{color:var(--ink)}

  .rows{display:flex;flex-direction:column;gap:5px}
  .req-row{display:grid;align-items:center;color:var(--white);font-size:5.6px;line-height:1.3}
  .req-name{display:flex;flex-direction:column;align-items:center;text-align:center;padding:3px 6px;gap:3px;font-weight:600}
  .req-desc,.req-risk{padding:3px 6px}
  .req-icon{width:15px;height:15px;flex:none}

  .tone-plum-900{background:var(--plum-900)}
  .tone-plum-800{background:var(--plum-800)}
  .tone-plum-700{background:var(--plum-700)}
  .tone-plum-600{background:var(--plum-600)}
  .tone-plum-500{background:var(--plum-500)}
  .tone-plum-300{background:var(--plum-300)}
  .tone-teal-900{background:var(--teal-900)}
  .tone-teal-800{background:var(--teal-800)}
  .tone-teal-600{background:var(--teal-600)}
  .tone-slate-800{background:var(--slate-800)}
  .tone-slate-600{background:var(--slate-600)}

  .wordmark{position:absolute;left:738px;top:782px;font-family:"Montserrat",Arial,sans-serif;font-weight:800;
    font-size:74px;letter-spacing:4px;color:var(--mark);line-height:1}
</style>
</head>
<body>

<svg class="folder" width="1200" height="930" viewBox="0 0 1200 930" aria-hidden="true">
  <defs>
    <linearGradient id="tabGrad" x1="0" y1="0" x2="1" y2="0">
      <stop offset="0" stop-color="var(--orange)"/>
      <stop offset="1" stop-color="var(--orange-red)"/>
    </linearGradient>
    <linearGradient id="panelGrad" x1="0" y1="0" x2="0" y2="1">
      <stop offset="0" stop-color="var(--panel)"/>
      <stop offset="1" stop-color="var(--panel-light)"/>
    </linearGradient>
    <clipPath id="folderShape">
      <path d="M48,80 Q48,48 80,48 L460,48 Q486,48 496,72 L516,128 Q526,156 556,156 L1122,156 Q1164,156 1164,198 L1164,860 Q1164,894 1130,894 L82,894 Q48,894 48,860 Z"/>
    </clipPath>
  </defs>
  <g clip-path="url(#folderShape)">
    <rect x="0" y="0" width="1200" height="296" fill="url(#tabGrad)"/>
    <rect x="0" y="296" width="1200" height="640" fill="url(#panelGrad)"/>
  </g>
</svg>

<div class="brand">
  <span class="brand-dot"></span>
  <span class="brand-name">Voltrix</span>
</div>

<div class="category category--robust">Robust</div>
<div class="category category--integration">Integration into existing environments</div>
<div class="category category--security">Security</div>
<div class="category category--fleet">Fleet management</div>

<svg class="connectors" width="1200" height="930" viewBox="0 0 1200 930" aria-hidden="true">
  <g fill="none" stroke="var(--ink)" stroke-width="1.5">
    <path d="M413,280 V302 H330 V318"/>
    <path d="M572,280 V300 H430 V346"/>
    <path d="M800,280 V614 H770"/>
    <path d="M1128,280 V346"/>
  </g>
  <g fill="var(--plum-900)">
    <circle cx="413" cy="280" r="4"/>
    <circle cx="800" cy="280" r="4" fill="var(--slate-700)"/>
    <circle cx="1128" cy="280" r="4"/>
  </g>
  <circle cx="572" cy="280" r="4" fill="var(--teal-900)"/>
</svg>

<!-- Robust -->
<section class="req-table req-table--robust">
  <div class="table-head"><span>Requirement</span><span>Description</span><span>Risks when not implemented</span></div>
  <div class="rows">
    <div class="req-row tone-plum-900" style="height:67px">
      <div class="req-name"><svg class="req-icon" viewBox="0 0 16 16"><circle cx="8" cy="8" r="8" fill="#fff"/><rect x="5" y="4" width="6" height="8" rx="1" fill="var(--plum-900)"/></svg>Is immune to power and network loss mid-update in order to avoid any bricked devices</div>
      <div class="req-desc">Atomic installs (full image over package-based) where an update is always fully installed or not at all avoids the possibility of a device becoming unbootable due to interruptions of an update. No software component ever sees a partially installed update</div>
      <div class="req-risk">Devices may be bricked when an update is interrupted due to poor network connectivity or power loss and may become unusable. Non-atomic updates also run the risk of inconsistency across a fleet of devices and becomes unmanageable when production does not match test environments</div>
    </div>
    <div class="req-row tone-plum-800" style="height:72px">
      <div class="req-name"><svg class="req-icon" viewBox="0 0 16 16"><circle cx="8" cy="8" r="8" fill="#fff"/><path d="M5 8a3 3 0 1 0 1-2.2M4.5 4.5v2.3h2.3" fill="none" stroke="var(--plum-800)" stroke-width="1.4"/></svg>Rollback to previous working version is built-in and automatic with sanity checks post-installation</div>
      <div class="req-desc">Dual A/B partition is one of the most reliable and simple approaches for built-in rollback where the update is written to the inactive root filesystem partition and the bootloader is configured to boot from it and then the modified system reboots. Should the updater come up it will try to report the success of the deployment to the management server. If this fails it will automatically rollback.</div>
      <div class="req-risk">If an update fails for any reason with no ability to rollback to the last working version, sending a technician to the field where the device resides will be costly.</div>
    </div>
    <div class="req-row tone-plum-700" style="height:62px">
      <div class="req-name"><svg class="req-icon" viewBox="0 0 16 16"><circle cx="8" cy="8" r="8" fill="#fff"/><path d="M4.5 8.5l2.2 2.2 4.8-5" fill="none" stroke="var(--plum-700)" stroke-width="1.6"/></svg>Integrity check to avoid corruption</div>
      <div class="req-desc">Make sure the update artifact is not corrupted, end-to-end from build system to device, due to any transfer or hardware issues</div>
      <div class="req-risk">Intermittent application malfunction, application not starting or device bricking due to random modifications of the update.</div>
    </div>
    <div class="req-row tone-plum-300" style="height:72px">
      <div class="req-name"><svg class="req-icon" viewBox="0 0 16 16"><circle cx="8" cy="8" r="8" fill="#fff"/><rect x="5" y="5" width="6" height="6" fill="var(--plum-300)"/></svg>Compatibility check</div>
      <div class="req-desc">Verifies that the software update can run on the target devices. For example, the CPU architecture of the devices are supported by the software update.</div>
      <div class="req-risk">Application fails to start or the device gets bricked immediately because the software is built for the wrong device type. This is in particular an issue when multiple revisions of devices and software are introduced, and software updates only support a subset of the devices.</div>
    </div>
    <div class="req-row tone-plum-700" style="height:50px">
      <div class="req-name"><svg class="req-icon" viewBox="0 0 16 16"><circle cx="8" cy="8" r="8" fill="#fff"/><path d="M8 4v6M5.5 7.5L8 10l2.5-2.5M5 12h6" fill="none" stroke="var(--plum-700)" stroke-width="1.4"/></svg>Ensure another update can be deployed</div>
      <div class="req-desc">After an update has been deployed, make sure that another update can be deployed by making sure that the deployment server can be reached after the update. Otherwise a rollback should be performed.</div>
      <div class="req-risk">If an update makes a device malfunction in certain ways such as losing network connectivity, the device can never be fixed and is effectively bricked.</div>
    </div>
    <div class="req-row tone-plum-600" style="height:72px">
      <div class="req-name"><svg class="req-icon" viewBox="0 0 16 16"><circle cx="8" cy="8" r="8" fill="#fff"/><path d="M4.5 8.5l2.2 2.2 4.8-5" fill="none" stroke="var(--plum-600)" stroke-width="1.8"/></svg>Custom sanity checks after the update</div>
      <div class="req-desc">Even though a device boots, it does not mean that its application works properly. For example, the UI framework may not be brought up. Custom sanity checks are automatically run after the update and the updater automatically rolls back the update if they do not all pass.</div>
      <div class="req-risk">The device may be unusable to the end user because important applications are not brought up after the update or key services are malfunctioning.</div>
    </div>
    <div class="req-row tone-plum-500" style="height:58px">
      <div class="req-name"><svg class="req-icon" viewBox="0 0 16 16"><circle cx="8" cy="8" r="8" fill="#fff"/><path d="M6 5L3.5 8 6 11M10 5l2.5 3L10 11" fill="none" stroke="var(--plum-500)" stroke-width="1.4"/></svg>Well maintained code and high code quality</div>
      <div class="req-desc">The updater is a critical component to an embedded system and needs to be well tested and widely used across a wide variety of use cases so the code maintains a high quality level.</div>
      <div class="req-risk">Bugs in the updater itself can not only brick devices but also expose serious security vulnerabilities to the devices.</div>
    </div>
  </div>
</section>

<!-- Integration into existing environments -->
<section class="req-table req-table--integration">
  <div class="table-head"><span>Requirement</span><span>Description</span><span>Risks when not implemented</span></div>
  <div class="rows">
    <div class="req-row tone-teal-900" style="height:48px">
      <div class="req-name"><svg class="req-icon" viewBox="0 0 16 16"><circle cx="8" cy="8" r="8" fill="#fff"/><circle cx="8" cy="8" r="3" fill="none" stroke="var(--teal-900)" stroke-width="1.5"/></svg>Existing development build system integration</div>
      <div class="req-desc">The update process should integrate with existing OSes, development tools and popular build systems like the Kestrel Build Project.</div>
      <div class="req-risk">Pushback from the development team if the updater dictates the tools they need to use, for example a "rip and replace" solution that dictates the embedded OS, language or how updates are packaged.</div>
    </div>
    <div class="req-row tone-teal-800" style="height:58px">
      <div class="req-name"><svg class="req-icon" viewBox="0 0 16 16"><circle cx="8" cy="8" r="8" fill="#fff"/><path d="M5 11l6-6M7 5h4v4" fill="none" stroke="var(--teal-800)" stroke-width="1.5"/></svg>Standalone deployments</div>
      <div class="req-desc">While OTA is the desired mechanism, many devices will initially require standalone deployments with an update via a USB or SD Card</div>
      <div class="req-risk">If devices without wireless network connectivity cannot be updated, they have an increased security risk and will almost certainly be vulnerable to attacks of publicly known vulnerabilities over time.</div>
    </div>
    <div class="req-row tone-teal-600" style="height:79px">
      <div class="req-name"><svg class="req-icon" viewBox="0 0 16 16"><circle cx="8" cy="8" r="8" fill="#fff"/><rect x="4.5" y="6" width="7" height="4" fill="var(--teal-600)"/></svg>Raw flash support</div>
      <div class="req-desc">Embedded systems can use a variety of storage, including raw NAND flash, eMMC and SPI-NOR. Besides supporting all these, the updater must not make unnecessary writes to the storage because this will quickly wear out the flash.</div>
      <div class="req-risk">If the updater does not support all embedded storage types used, some devices may not be able to update and thus leave a security issue as software vulnerabilities become public over time. If the updater does not take into account the limited wear requirement of flash-based devices, the devices will get bricked over time.</div>
    </div>
  </div>
</section>

<!-- Security -->
<section class="req-table req-table--security">
  <div class="table-head"><span>Requirement</span><span>Description</span><span>Risks when not implemented</span></div>
  <div class="rows">
    <div class="req-row tone-slate-800" style="height:64px">
      <div class="req-name"><svg class="req-icon" viewBox="0 0 16 16"><circle cx="8" cy="8" r="8" fill="#fff"/><rect x="5" y="7.5" width="6" height="4.5" fill="var(--slate-800)"/><path d="M6.2 7.5V6a1.8 1.8 0 0 1 3.6 0v1.5" fill="none" stroke="var(--slate-800)" stroke-width="1.2"/></svg>Secure communications between the management server and the client running on the device</div>
      <div class="req-desc">Use of secure and bi-directionally authenticated communication between the client/server (e.g. TLS)</div>
      <div class="req-risk">The update can be modified while in transit from the update server to the device, enabling an attacker to inject malicious code, steal data and take over the device. This attack is particularly susceptible over wireless networks. The attacker could also imitate the update server, forcing a malicious update to be installed at their choosing.</div>
    </div>
    <div class="req-row tone-slate-600" style="height:67px">
      <div class="req-name"><svg class="req-icon" viewBox="0 0 16 16"><circle cx="8" cy="8" r="8" fill="#fff"/><path d="M5 4h6v8H5zM6.5 9.5l1.5-1 1.5 1" fill="none" stroke="var(--slate-600)" stroke-width="1.2"/></svg>Authenticity of update images with code signing</div>
      <div class="req-desc">End-to-end signature management to authenticate it is an authorized and trusted update</div>
      <div class="req-risk">Lack of digital signatures/code signing allows attackers to reprogram sensitive components of the embedded system by modifying a valid update, enabling attackers to inject malicious code or take over the device.</div>
    </div>
  </div>
</section>

<!-- Fleet management -->
<section class="req-table req-table--fleet">
  <div class="table-head"><span>Requirement</span><span>Description</span><span>Risks when not implemented</span></div>
  <div class="rows">
    <div class="req-row tone-plum-900" style="height:52px">
      <div class="req-name"><svg class="req-icon" viewBox="0 0 16 16"><circle cx="8" cy="8" r="8" fill="#fff"/><rect x="5" y="4.5" width="6" height="2.5" fill="var(--plum-900)"/><rect x="5" y="8" width="6" height="2.5" fill="var(--plum-900)"/></svg>Deployment management server</div>
      <div class="req-desc">Ability to automate deployment across a fleet of devices</div>
      <div class="req-risk">If devices need to be updated one-by-one, deploying updates will be extremely costly or not carried out at all.</div>
    </div>
    <div class="req-row tone-plum-700" style="height:82px">
      <div class="req-name"><svg class="req-icon" viewBox="0 0 16 16"><circle cx="8" cy="8" r="8" fill="#fff"/><g fill="var(--plum-700)"><rect x="4.5" y="4.5" width="2" height="2"/><rect x="7" y="4.5" width="2" height="2"/><rect x="9.5" y="4.5" width="2" height="2"/><rect x="4.5" y="7" width="2" height="2"/><rect x="7" y="7" width="2" height="2"/><rect x="9.5" y="7" width="2" height="2"/><rect x="4.5" y="9.5" width="2" height="2"/><rect x="7" y="9.5" width="2" height="2"/><rect x="9.5" y="9.5" width="2" height="2"/></g></svg>Device inventory</div>
      <div class="req-desc">Ability to list all devices, through an UI and REST API, together with key inventory information such as network addresses, product version and model and when it last connected to the server infrastructure.</div>
      <div class="req-risk">In order to plan for software updates, you need to know what is out there already. This will make it possible to know if the installed software is compatible with the desired update. It is also critical to know which software is installed on all the devices in order to discover which devices are vulnerable to known vulnerabilities and CVEs so that they can be updated.</div>
    </div>
    <div class="req-row tone-plum-300" style="height:48px">
      <div class="req-name"><svg class="req-icon" viewBox="0 0 16 16"><circle cx="8" cy="8" r="8" fill="#fff"/><path d="M5 4h6v8H5zM6.5 6.5h3M6.5 8.5h3" fill="none" stroke="var(--plum-300)" stroke-width="1.1"/></svg>Deployment logs</div>
      <div class="req-desc">Diagnostics logs from devices that are captured as a deployment is carried out</div>
      <div class="req-risk">If a deployment fails across one or more devices and there are no logs, issues are very hard to diagnose and fix.</div>
    </div>
    <div class="req-row tone-plum-800" style="height:74px">
      <div class="req-name"><svg class="req-icon" viewBox="0 0 16 16"><circle cx="8" cy="8" r="8" fill="#fff"/><path d="M5 11.5V9M8 11.5V5.5M11 11.5V7.5" fill="none" stroke="var(--plum-800)" stroke-width="1.6"/></svg>Deployment status reports</div>
      <div class="req-desc">An overall status of the deployment, such as how many devices succeeded and failed the deployment as well as which devices failed.</div>
      <div class="req-risk">If it is not possible to know if a deployment succeeds or fails and on which devices, deploying updates is very risky as bricking devices can go unnoticed for a very long time. The only way to see failures in this case is when end users report them which leads to a very bad customer experience and an expensive support burden.</div>
    </div>
  </div>
</section>

<div class="wordmark">VOLTRIX</div>

</body>
</html>
```